Presentation folder for RKW
The attached file is our previous folder design. We are looking for something updated and fresh and professional not too busy. Must be two color blue and black.

```html
<!DOCTYPE html>
<html lang="en">
<head>
<meta charset="utf-8">
<title>RKW Dental Plan – Presentation Folder</title>
<link rel="stylesheet" href="https://fonts.googleapis.com/css2?family=Arimo:wght@400;700&family=Tinos&display=swap">
<style>
  :root {
    --stage: #000000;
    --brand-blue: #1f6db5;
    --brand-blue-deep: #14528c;
    --pocket-blue: #1a5fa0;
    --paper: #f4f5f6;
    --paper-shade: #d9dcdf;
    --pocket-paper: #e9ebed;
    --ink: #111111;
    --white: #ffffff;
  }
  * { margin: 0; padding: 0; box-sizing: border-box; }
  html, body { width: 1200px; height: 568px; overflow: hidden; background: var(--stage); }
  .canvas { position: relative; width: 1200px; height: 568px; }

  .folder { position: absolute; display: flex; }
  .folder--closed { left: 48px; top: 62px; width: 520px; height: 420px; }
  .folder--open { left: 630px; top: 84px; width: 476px; height: 388px; }

  .panel { position: relative; flex: 1; overflow: hidden; }
  .panel--blue { background: linear-gradient(180deg, var(--brand-blue) 0%, var(--brand-blue-deep) 100%); color: var(--white); }
  .panel--paper { background: linear-gradient(90deg, var(--paper-shade) 0%, var(--paper) 40%, var(--white) 100%); color: var(--brand-blue); }

  .brand {
    position: absolute; display: flex; align-items: center; gap: 9px;
    font-family: "Arimo", Arial, sans-serif; font-weight: 700; line-height: 1;
    white-space: nowrap;
  }
  .brand__mark { width: 15px; height: 15px; background: currentColor; flex: none; }
  .brand__name { font-size: 25px; letter-spacing: -0.3px; }
  .brand--cover { left: 26px; top: 150px; }
  .brand--front { left: 30px; top: 150px; }
  .brand--pocket .brand__name { font-size: 21px; }
  .brand--pocket .brand__mark { width: 13px; height: 13px; }
  .brand--pocket { left: 20px; top: 80px; }

  .address {
    position: absolute; font-family: "Tinos", "Times New Roman", serif;
    font-size: 8.5px; line-height: 1.45; color: var(--white); white-space: nowrap;
  }
  .address--cover { left: 50px; top: 194px; }
  .address--pocket { left: 44px; top: 118px; }

  .web {
    position: absolute; font-family: "Tinos", "Times New Roman", serif;
    font-size: 12px; color: var(--ink); white-space: nowrap;
  }
  .web--front { left: 78px; bottom: 24px; }
  .web--pocket { left: 318px; bottom: 16px; font-size: 10px; }

  .pocket { position: absolute; left: 0; top: 0; width: 476px; height: 388px; }
  .pocket__left { fill: var(--pocket-blue); }
  .pocket__right { fill: var(--pocket-paper); }
</style>
</head>
<body>
<main class="canvas">

  <section class="folder folder--closed" aria-label="Folder outside spread">
    <div class="panel panel--blue">
      <div class="brand brand--cover"><span class="brand__mark"></span><span class="brand__name">RKW Dental Plan</span></div>
      <p class="address address--cover">Member Services Office<br>12 Harbor Street, Suite 4<br>Millbrook, CA 90000<br>Tel: 555 010 0100<br>Fax: 555 010 0101</p>
    </div>
    <div class="panel panel--paper">
      <div class="brand brand--front"><span class="brand__mark"></span><span class="brand__name">RKW Dental Plan</span></div>
      <p class="web web--front">www.rkwdental.com</p>
    </div>
  </section>

  <section class="folder folder--open" aria-label="Folder inside spread with pockets">
    <div class="panel panel--blue">
      <div class="brand brand--pocket"><span class="brand__mark"></span><span class="brand__name">RKW Dental Plan</span></div>
      <p class="address address--pocket">Member Services Office<br>12 Harbor Street, Suite 4<br>Millbrook, CA 90000<br>Tel: 555 010 0100<br>Fax: 555 010 0101</p>
    </div>
    <div class="panel panel--paper">
      <div class="brand brand--pocket"><span class="brand__mark"></span><span class="brand__name">RKW Dental Plan</span></div>
    </div>
    <svg class="pocket" viewBox="0 0 476 388" aria-hidden="true">
      <polygon class="pocket__left" points="0,270 200,270 238,300 238,388 0,388"/>
      <polygon class="pocket__right" points="238,300 276,270 476,270 476,388 238,388"/>
      <line x1="0" y1="270" x2="200" y2="270" stroke="#5d95cc" stroke-width="1"/>
      <line x1="276" y1="270" x2="476" y2="270" stroke="#c4c8cc" stroke-width="1"/>
      <polyline points="200,270 238,300 276,270" fill="none" stroke="#9aa0a6" stroke-width="1"/>
    </svg>
    <p class="web web--pocket">www.rkwdental.com</p>
  </section>

</main>
</body>
</html>
```